Dental Practice Billboard Design

We are a newer dental practice in need of a simple but appealing billboard for our growing dental practice to attract new patients. The practice is owned by husband and wife dentists and is family friendly in a small town in Kentucky. We try to be very friendly and caring to our patients. Would prefer a blue background for the billboard and our tooth logo to be prominent. We are partial to the Patua One font used in the image below but please feel free to tweak it as you deem necessary. The shape of the uppercase D and lowercase g are why we like that font, so fonts with a similarly shaped “D” and “g” would work as well. Please include our phone number (606) 847-3962. Please see our website Harlowfamilydentistry.com for more info on the practice if needed. Thank you! Looking forward to seeing your creation.
Updates

The dimensions will be 12ft x 24ft (3.6576m x 7.3152m). Apologies for not including this in the original prompt. Thank you all for your submissions.

Industry/Entity Type

Dental

Font styles to use
Other font styles liked:
• Patua One

Colors
0054AA
0677BA
7BADD7
CADEEF
E8F1F8
0094D4
00A9DD
6FCCEA
C7EBF8
E9F6FB
00AB8E
00BBA5
67D7C9
C6EFE9
E9F9F6
59FF00
82FF00
B8FF75
E3FFCB
F4FFEA

Requirements
Must have
• Phone number, website, Logo, Practice name “Harlow Family Dentistry”
Should not have
• A tagline or slogan

```html
<!DOCTYPE html>
<html lang="en">
<head>
<meta charset="utf-8">
<title>Harlow Family Dentistry Billboard</title>
<link rel="stylesheet" href="https://fonts.googleapis.com/css2?family=Patua+One&family=Fira+Sans:wght@600&display=swap">
<style>
  :root {
    --page-bg: #e8f1f8;
    --navy-deep: #062a5c;
    --navy: #0a3a80;
    --blue: #0054aa;
    --photo-tone: #1356b0;
    --photo-tone-soft: #0d4796;
    --green: #17b31a;
    --white: #ffffff;
  }
  html, body {
    margin: 0;
    padding: 0;
    width: 1200px;
    height: 858px;
    overflow: hidden;
    background: var(--page-bg);
  }
  .billboard {
    position: absolute;
    left: 20px;
    top: 139px;
    width: 1160px;
    height: 580px;
    overflow: hidden;
    background: radial-gradient(ellipse at 45% 20%, var(--navy) 0%, var(--navy-deep) 75%);
    font-family: "Patua One", Georgia, serif;
    color: var(--white);
  }
  .portrait {
    position: absolute;
    top: 0;
    height: 580px;
    opacity: 0.75;
  }
  .portrait--left {
    left: 0;
    width: 300px;
    background: linear-gradient(90deg, var(--photo-tone) 0%, var(--photo-tone-soft) 70%, rgba(13,71,150,0) 100%);
  }
  .portrait--right {
    right: 0;
    width: 230px;
    background: linear-gradient(270deg, var(--photo-tone) 0%, var(--photo-tone-soft) 65%, rgba(13,71,150,0) 100%);
  }
  .brand-mark {
    position: absolute;
    left: 250px;
    top: 105px;
    width: 170px;
    height: 170px;
    border-radius: 50%;
    background: var(--green);
  }
  .brand-name {
    position: absolute;
    left: 450px;
    top: 100px;
    margin: 0;
    font-weight: 400;
    line-height: 1;
  }
  .brand-name__primary {
    display: block;
    font-size: 128px;
  }
  .brand-name__secondary {
    display: block;
    font-size: 58px;
    margin-top: 6px;
    margin-left: -10px;
  }
  .contact-band {
    position: absolute;
    left: 0;
    top: 0;
    width: 1160px;
    height: 580px;
  }
  .contact {
    position: absolute;
    left: 50px;
    bottom: 24px;
    display: flex;
    align-items: baseline;
    gap: 26px;
    white-space: nowrap;
  }
  .contact__phone {
    font-family: "Fira Sans", Arial, sans-serif;
    font-weight: 600;
    font-size: 70px;
  }
  .contact__dot {
    width: 12px;
    height: 12px;
    border-radius: 50%;
    background: var(--white);
    align-self: center;
    margin-top: 14px;
  }
  .contact__web { font-size: 42px; }
</style>
</head>
<body>
  <main class="billboard">
    <div class="portrait portrait--left" role="img" aria-label="Photo of the smiling male dentist, tinted blue"></div>
    <div class="portrait portrait--right" role="img" aria-label="Photo of the smiling female dentist, tinted blue"></div>

    <div class="brand-mark" aria-hidden="true"></div>
    <h1 class="brand-name">
      <span class="brand-name__primary">Harlow</span>
      <span class="brand-name__secondary">Family Dentistry</span>
    </h1>

    <svg class="contact-band" viewBox="0 0 1160 580" aria-hidden="true">
      <path d="M0 370 Q 560 520 1160 450 L1160 580 L0 580 Z" fill="var(--green)"/>
    </svg>

    <div class="contact">
      <span class="contact__phone">(606) 847-3962</span>
      <span class="contact__dot"></span>
      <span class="contact__web">Harlowfamilydentistry.com</span>
    </div>
  </main>
</body>
</html>
```